Would like a Northwest feel to the look, something NOT typical of what you would see on a typical Home Inspectors logo. Real estate cards all the same as well, and would like to stand out. Earthy, green, Northwest. Sadly a portrait seems to be a requirement (see the attached). I inspect residential homes for buyers and sellers.

Target Market(s)

Home Buyers and Sellers

Industry/Entity Type

Home Inspection

Contact Information for Business Card

See description
Note: The name Corvaneth is a Chinook word that means 'Friend'. Please do not associate the name with the Whale that shows up on 99% of google searches.

Logo Text

Corvaneth Home Inspections

Colors

Designer to choose colors to be used in the design.

Requirements
Must have
• Phone Num: 541-672-8153
• Address: 732 SW 219th Av Num 618
• Portland, Oregon 97388
• Email: glen@corvanethhomeinspection.example
• Website: www.CorvanethHomeInspection.example
• Additional Note: Need to add the Obravex logo (icon). It should be small and not the focus of the card. The logo can be found at Obravex.example
Nice to have
• I am open
Should not have
• Cant think of anything

```html
<!DOCTYPE html>
<html lang="en">
<head>
<meta charset="utf-8">
<title>Corvaneth Home Inspections – Business Card</title>
<link href="https://fonts.googleapis.com/css2?family=Montserrat:wght@500;600;700&family=Work+Sans:wght@400;500&display=swap" rel="stylesheet">
<style>
  :root {
    --navy: #24306e;
    --navy-deep: #1f2a66;
    --green: #3bb54a;
    --white: #ffffff;
    --backdrop: #e9eaee;
    --silver: #b9bfd6;
    --photo-a: #c9c2b2;
    --photo-b: #8d8a7b;
  }
  * { margin: 0; padding: 0; box-sizing: border-box; }
  html, body { width: 1200px; height: 900px; overflow: hidden; }
  body { background: var(--backdrop); position: relative; font-family: "Work Sans", sans-serif; }

  .card {
    position: absolute;
    width: 620px; height: 354px;
    border-radius: 16px;
    overflow: hidden;
    box-shadow: 0 10px 30px rgba(20, 25, 60, 0.18);
  }

  /* back side */
  .card-back { left: 500px; top: 60px; background: var(--navy-deep); }
  .card-back .wordmark {
    position: absolute; left: 0; right: 0; top: 140px;
    text-align: center;
    font-family: "Montserrat", sans-serif; font-weight: 600;
    font-size: 54px; letter-spacing: 2px;
    color: var(--silver);
  }
  .card-back .member-badge { position: absolute; right: 34px; bottom: 30px; }

  /* front side */
  .card-front { left: 80px; top: 470px; background: var(--white); }
  .card-front .wordmark {
    position: absolute; left: 32px; top: 34px;
    display: flex; align-items: center; gap: 12px;
    font-family: "Montserrat", sans-serif; font-weight: 600;
    font-size: 44px; letter-spacing: 1px; color: var(--navy);
  }
  .wordmark .dot { width: 16px; height: 16px; border-radius: 50%; background: var(--green); }

  .portrait {
    position: absolute; left: 474px; top: 20px;
    width: 100px; height: 100px; border-radius: 50%;
    border: 2px solid var(--navy);
    background: radial-gradient(circle at 50% 40%, var(--photo-a), var(--photo-b));
  }

  .divider { position: absolute; left: 30px; top: 166px; width: 552px; height: 1.5px; background: var(--navy); }

  .person-name {
    position: absolute; right: 38px; top: 132px;
    font-family: "Montserrat", sans-serif; font-weight: 700;
    font-size: 22px; line-height: 27px; letter-spacing: 1.5px; color: var(--navy);
    white-space: nowrap;
  }
  .person-role {
    position: absolute; right: 38px; top: 172px;
    font-size: 15px; line-height: 18px; color: var(--green);
  }

  .side-tab { position: absolute; right: 0; top: 150px; width: 12px; height: 44px; border-radius: 8px 0 0 8px; background: var(--green); }

  .contact { position: absolute; left: 32px; top: 176px; color: var(--navy); font-size: 13.5px; line-height: 18px; }
  .contact .address { margin-bottom: 6px; }
  .contact .line { display: flex; align-items: center; gap: 9px; }
  .contact .line svg { flex: none; }

  .wave { position: absolute; left: 0; bottom: 0; }
</style>
</head>
<body>

  <section class="card card-back" aria-label="Business card back">
    <div class="wordmark">CORVANETH</div>
    <svg class="member-badge" width="62" height="62" viewBox="0 0 62 62" role="img" aria-label="Obravex membership badge">
      <circle cx="31" cy="31" r="28" fill="none" stroke="var(--white)" stroke-width="2.5"/>
    </svg>
  </section>

  <section class="card card-front" aria-label="Business card front">
    <div class="wordmark"><span class="dot"></span>CORVANETH</div>

    <div class="portrait" role="img" aria-label="Portrait photo of Marlen Ostrow"></div>

    <div class="person-name">MARLEN OSTROW</div>
    <div class="divider"></div>
    <div class="person-role">Director</div>
    <div class="side-tab"></div>

    <div class="contact">
      <div class="address">732 SW 219th Av Num 618<br>Portland, Oregon 97388</div>
      <div class="line">
        <svg width="11" height="11" viewBox="0 0 24 24"><path fill="var(--green)" d="M6.6 10.8a15 15 0 0 0 6.6 6.6l2.2-2.2c.3-.3.7-.4 1-.2 1.1.4 2.3.6 3.6.6.6 0 1 .4 1 1V20c0 .6-.4 1-1 1A17 17 0 0 1 3 4c0-.6.4-1 1-1h3.5c.6 0 1 .4 1 1 0 1.3.2 2.5.6 3.6.1.3 0 .7-.2 1z"/></svg>
        541-672-8153
      </div>
      <div class="line">
        <svg width="11" height="11" viewBox="0 0 24 24"><rect x="2" y="5" width="20" height="14" rx="2" fill="none" stroke="var(--green)" stroke-width="2.4"/><path d="M2 6l10 7 10-7" fill="none" stroke="var(--green)" stroke-width="2.4"/></svg>
        glen@corvanethhomeinspection.example
      </div>
      <div class="line">
        <svg width="11" height="11" viewBox="0 0 24 24"><circle cx="12" cy="12" r="10" fill="none" stroke="var(--green)" stroke-width="2.4"/><path d="M2 12h20M12 2c3 3 3 17 0 20M12 2c-3 3-3 17 0 20" fill="none" stroke="var(--green)" stroke-width="2"/></svg>
        www.CorvanethHomeInspection.example
      </div>
    </div>

    <svg class="wave" width="620" height="70" viewBox="0 0 620 70">
      <path d="M0,10 C140,46 300,64 430,48 S580,22 620,12 L620,70 L0,70 Z" fill="var(--green)"/>
      <path d="M0,19 C140,54 300,72 430,56 S580,30 620,21 L620,70 L0,70 Z" fill="var(--navy)"/>
    </svg>
  </section>

</body>
</html>
```